BRAMWELL Sofa Shop - Hipster Hero Header Design

I want to use the 'Meridale' theme on Storvik

https://meridale-theme-basic.storvikshop.example/
https://themes.storvikshop.example/themes/meridale/styles/plenwise/preview

The main, PRIMARY thing that I need designed is the top hero header to be customized to my shop. Please use the attached examples as a reference. I welcome creativity. I do like the hipster vibe. I'd like a sofa/Living Room theme.

****To be clear...I want a hipster header designed...I love the creative fonts on a filtered relevant photo*** I have placed attachments. Hipster fonts or a Badge, or some combo. If you need guidance please look at examples.

Words on design should be:

BRAMWELL SOFA SHOP.

(I will separately handle the functionality of the site.)
Thanks.
Updates

Please check my brief as I have streamlined my desires. I simply want a hero header designed and 3 buttons designed. Examples of hero headers are attached. Thanks. Added Saturday, September 26, 2015

Target Market(s)

Sofa Shoppers

Industry/Entity Type

Furniture Store

Number of Pages Required

1 page

Requirements
Nice to have
• Bramwell Sofa Shop
• https://meridale-theme-basic.storvikshop.example/

```html
<!DOCTYPE html>
<html lang="en">
<head>
<meta charset="utf-8">
<title>Bramwell Sofa Shop – Hero Header Options</title>
<link rel="stylesheet" href="https://fonts.googleapis.com/css2?family=Pathway+Gothic+One&family=Righteous&family=Oswald:wght@400;600&family=Syncopate:wght@400;700&display=swap">
<style>
  :root {
    --ink: #000000;
    --white: #ffffff;
    --cream: #f3ece0;
    --cyan: #49e6ff;
    --magenta: #ff2fd8;
    --room-dark: #1b130c;
    --room-mid: #5a4026;
    --room-warm: #a9804d;
    --room-light: #e2c79a;
  }
  * { box-sizing: border-box; margin: 0; padding: 0; }
  html, body {
    width: 1200px;
    height: 2600px;
    overflow: hidden;
    background: var(--ink);
  }
  .sheet {
    width: 1200px;
    height: 2600px;
    display: flex;
    flex-direction: column;
  }
  .option {
    position: relative;
    height: 650px;
    display: flex;
    flex-direction: column;
  }
  .option-label {
    height: 36px;
    padding: 6px 10px;
    font: 400 22px/24px "Oswald", sans-serif;
    color: var(--white);
    background: var(--ink);
  }
  .hero {
    position: relative;
    flex: 1;
    overflow: hidden;
  }
  .hero-photo {
    position: absolute;
    inset: 0;
    background:
      radial-gradient(ellipse 22% 18% at 50% 14%, rgba(226,199,154,.55), transparent 70%),
      radial-gradient(ellipse 30% 40% at 50% 55%, rgba(169,128,77,.55), transparent 75%),
      linear-gradient(90deg, var(--room-dark) 0%, var(--room-mid) 18%, var(--room-warm) 40%, var(--room-light) 52%, var(--room-warm) 64%, var(--room-mid) 82%, var(--room-dark) 100%);
  }
  .hero-photo::after {
    content: "";
    position: absolute;
    inset: 0;
    background: linear-gradient(180deg, rgba(0,0,0,.45) 0%, rgba(0,0,0,.15) 45%, rgba(0,0,0,.55) 100%);
  }
  .nav {
    position: absolute;
    display: flex;
    gap: 22px;
    font: 400 15px/1 "Oswald", sans-serif;
    letter-spacing: 1px;
    color: var(--white);
    text-transform: uppercase;
  }
  .title, .tagline {
    position: absolute;
    color: var(--white);
    white-space: nowrap;
  }

  /* Option 5 */
  .opt-5 .nav { top: 20px; left: 22px; }
  .opt-5 .title {
    top: 170px; left: 0; right: 0; text-align: center;
    font: 400 118px/1 "Pathway Gothic One", sans-serif;
  }
  .opt-5 .tagline {
    top: 290px; right: 100px;
    font: 400 64px/1 "Pathway Gothic One", sans-serif;
  }

  /* Option 6 */
  .opt-6 .nav { top: 36px; right: 32px; font-weight: 600; }
  .opt-6 .title {
    top: 200px; left: 0; right: 0; text-align: center;
    font: 400 66px/1 "Righteous", sans-serif;
    letter-spacing: 2px;
    text-shadow: 0 0 6px var(--cyan), 0 0 16px var(--cyan), 3px 3px 0 rgba(0,0,0,.4);
  }
  .opt-6 .tagline {
    top: 300px; left: 0; right: 0; text-align: center;
    font: 600 40px/1 "Oswald", sans-serif;
    letter-spacing: 1px;
  }

  /* Option 7 */
  .opt-7 .nav { top: 18px; left: 0; right: 0; justify-content: center; }
  .opt-7 .nav-rule {
    position: absolute; top: 50px; left: 460px; width: 340px; height: 2px;
    background: var(--cream);
  }
  .opt-7 .title {
    top: 190px; left: 0; right: 0; text-align: center;
    font: 400 120px/1 "Pathway Gothic One", sans-serif;
    color: var(--cream);
  }
  .opt-7 .tagline {
    top: 316px; left: 0; right: 0; text-align: center;
    font: 400 66px/1 "Pathway Gothic One", sans-serif;
    color: var(--cream);
  }

  /* Option 8 */
  .opt-8 .title {
    top: 214px; left: 0; right: 0; text-align: center;
    font: 700 44px/1 "Syncopate", sans-serif;
    letter-spacing: 6px;
  }
  .opt-8 .tagline {
    top: 282px; left: 0; right: 0; text-align: center;
    font: 700 24px/1 "Syncopate", sans-serif;
    letter-spacing: 4px;
    color: var(--magenta);
  }
  .opt-8 .nav-rule {
    position: absolute; top: 464px; left: 440px; width: 360px; height: 3px;
    background: var(--magenta);
  }
  .opt-8 .nav {
    top: 480px; left: 0; right: 0; justify-content: center; gap: 28px;
    font: 400 15px/1 "Syncopate", sans-serif; letter-spacing: 3px;
  }
</style>
</head>
<body>
<main class="sheet">

  <section class="option opt-5">
    <div class="option-label">Option #5</div>
    <div class="hero">
      <div class="hero-photo" role="img" aria-label="Warm-toned photo of an ornate living room with sofas, tall curtained windows and a crystal chandelier"></div>
      <nav class="nav"><span>About</span><span>Products</span><span>Contact</span></nav>
      <h1 class="title">The BRAMWELL SOFA SHOP</h1>
      <p class="tagline">The Best Sofas for Less</p>
    </div>
  </section>

  <section class="option opt-6">
    <div class="option-label">Option #6</div>
    <div class="hero">
      <div class="hero-photo" role="img" aria-label="Warm-toned photo of an ornate living room with sofas, tall curtained windows and a crystal chandelier"></div>
      <nav class="nav"><span>About</span><span>Products</span><span>Contact</span></nav>
      <h1 class="title">THE BRAMWELL SOFA SHOP</h1>
      <p class="tagline">THE BEST SOFAS FOR LESS</p>
    </div>
  </section>

  <section class="option opt-7">
    <div class="option-label">Option #7</div>
    <div class="hero">
      <div class="hero-photo" role="img" aria-label="Warm-toned photo of an ornate living room with sofas, tall curtained windows and a crystal chandelier"></div>
      <nav class="nav"><span>About</span><span>Products</span><span>Contact</span></nav>
      <div class="nav-rule"></div>
      <h1 class="title">The BRAMWELL SOFA SHOP</h1>
      <p class="tagline">The Best Sofas for Less</p>
    </div>
  </section>

  <section class="option opt-8">
    <div class="option-label">Option #8</div>
    <div class="hero">
      <div class="hero-photo" role="img" aria-label="Warm-toned photo of an ornate living room with sofas, tall curtained windows and a crystal chandelier"></div>
      <h1 class="title">THE BRAMWELL SOFA SHOP</h1>
      <p class="tagline">THE BEST SOFAS FOR LESS</p>
      <div class="nav-rule"></div>
      <nav class="nav"><span>About</span><span>Products</span><span>Contact</span></nav>
    </div>
  </section>

</main>
</body>
</html>
```